Business Card Design Project

I need a business card design for a new business called Tolland Insurance Services. I am a small insurance broker that will provide business insurance services mostly to contractors and small businesses. My business is all about customer service and assistance rather than being a price driven/focused business. I want my business card to be professional giving the impression that I am larger than one person but not a corporate company. I have attached a copy of my logo.
Updates

Hi all

I have been advised that I need to show the following info for compliance reasons on my card. It only has to be small.

Can you please include either front or back:

Tolland Insurance Services Pty Ltd [ABN 61827405193] AR No 586714 as Authorised Representative of Brackford Insurance Group Pty Ltd ACN 274 906 518 ABN 82 274 906 518 AFS Licence No 718264

Reason: I need a further change to be made to the design. I need the contact number of 1300476815 added to the business card.

Hi All

I need one last change made to the card.

Can you please include the phone number 1300476815 to the card. If possible can this be made fairly clear on the card, either large on the back or another design idea you may have.

Target Market(s)

30+ Professionals

Industry/Entity Type

Insurance

Requirements
Must have
• I want a double sided design. My details to go on the card are as follows:

Dylan Tolland QRPSUV (Snr Assoc.) CIP
Director
PO Box 872, Kestrelvale SA 5091
Phone: 0438 617 204
Fax 08 8397 2418
Email: dylan@tollandinsure.example
Website: http://www.tollandinsure.example
Twitter: Tollandinsure
Facebook: facebook.com/tollandinsure

```html
<!DOCTYPE html>
<html lang="en">
<head>
<meta charset="utf-8">
<title>Tolland Insurance Services – Business Card</title>
<link href="https://fonts.googleapis.com/css2?family=Open+Sans:wght@400;600;700&display=swap" rel="stylesheet">
<style>
  :root {
    --bg: #d4d4d4;
    --card: #fbfbfa;
    --ink: #1c1c1c;
    --brand-red: #d8262f;
    --label: #333333;
  }
  * { box-sizing: border-box; margin: 0; padding: 0; }
  html, body { width: 1200px; height: 900px; overflow: hidden; }
  body {
    background: var(--bg);
    font-family: "Open Sans", Arial, sans-serif;
    color: var(--ink);
    position: relative;
  }
  .card {
    position: absolute;
    width: 540px;
    height: 310px;
    background: var(--card);
    box-shadow: 0 3px 10px rgba(0,0,0,0.25);
  }
  .card--front { left: 50px; top: 150px; }
  .card--back { left: 610px; top: 440px; }

  .side-label {
    position: absolute;
    font-size: 13px;
    letter-spacing: 0.5px;
    color: var(--label);
    text-transform: uppercase;
  }
  .side-label--front { left: 540px; top: 466px; }
  .side-label--back { left: 1105px; top: 756px; }

  .wordmark {
    position: absolute;
    left: 110px;
    top: 40px;
    display: flex;
    align-items: center;
    gap: 12px;
  }
  .wordmark__dot {
    width: 34px; height: 34px;
    border-radius: 50%;
    background: var(--brand-red);
  }
  .wordmark__name {
    font-size: 38px;
    font-weight: 600;
    color: var(--brand-red);
    letter-spacing: -0.5px;
  }

  .holder {
    position: absolute;
    right: 70px;
    top: 118px;
    text-align: center;
    font-weight: 700;
    font-size: 13px;
    line-height: 1.35;
  }

  .contact {
    position: absolute;
    left: 172px;
    top: 176px;
    font-size: 12.5px;
    line-height: 1.45;
    white-space: nowrap;
  }
  .contact__hotline {
    font-weight: 700;
    font-size: 14px;
    color: var(--brand-red);
  }

  .back-mark {
    position: absolute;
    left: 0; right: 0;
    top: 40px;
    text-align: center;
    font-size: 17px;
    font-weight: 600;
    color: var(--brand-red);
  }
  .compliance {
    position: absolute;
    left: 0; right: 0;
    top: 96px;
    text-align: center;
    font-size: 15.5px;
    line-height: 1.4;
    padding: 0 30px;
  }
</style>
</head>
<body>
  <section class="card card--front">
    <div class="wordmark">
      <span class="wordmark__dot"></span>
      <span class="wordmark__name">tolland insurance</span>
    </div>
    <div class="holder">
      Dylan Tolland QRPSUV (Snr Assoc.) CIP<br>
      Director
    </div>
    <div class="contact">
      PO Box 872, Kestrelvale SA 5091<br>
      Phone: 0438 617 204, <span class="contact__hotline">1300 476 815</span> [Fax] 08 8397 2418<br>
      Email: dylan@tollandinsure.example<br>
      Website: http://www.tollandinsure.example<br>
      Twitter: Tollandinsure<br>
      Facebook: facebook.com/tollandinsure
    </div>
  </section>
  <span class="side-label side-label--front">Front</span>

  <section class="card card--back">
    <div class="back-mark">tolland insurance</div>
    <p class="compliance">
      Tolland Insurance Services Pty Ltd<br>
      [ABN 61827405193]<br>
      AR No 586714 as Authorised<br>
      Representative of Brackford Insurance Group<br>
      Pty Ltd ACN 274 906 518 ABN 82 274 906 518 AFS<br>
      Licence No 718264
    </p>
  </section>
  <span class="side-label side-label--back">Back</span>
</body>
</html>
```